Pelton|Marsh & Quillan business card contest

We need a logo for an upscale boutique diversified company involved in real estate, investments, cattle, and more. Our businesses DO NOT need to be reflected in the business card nor do we want them noted. This is our logo and colors and we love our logo and colors. Our logo looks best against a black background and we like to include the firm name in our logo usage. importantly, the names Pelton and Marsh are separated by | not / and we use an ampersand not the word and.
On the front of the card, we want to include:
company logo and name (Pelton|Marsh & Quillan)
on the back, we would definitely include:
address, email, cell #
logo and name (smaller size than front)

The variable will be location of individual name and title (mine for example is ) - whether on the front OR on the back. interested in variations from which to choose
Dr. Neil R. Whitcombe, CFA
Scientifique des Fusées Financières

we would like to use contemporary symbols for address, email address, cell # with an option for web site that we do not intend to use initially. we like two sided cards and believe this design should use four rounded corners with the standard size. we prefer thicker card stock and may look at metal.

```html
<!DOCTYPE html>
<html lang="en">
<head>
<meta charset="utf-8">
<title>Pelton|Marsh &amp; Quillan – Business Card</title>
<link href="https://fonts.googleapis.com/css2?family=Raleway:wght@400;500&family=Open+Sans:wght@400&display=swap" rel="stylesheet">
<style>
  :root {
    --backdrop: #6e6e6e;
    --card-white: #ffffff;
    --card-grey: #dcdcdc;
    --band-black: #000000;
    --back-black: #0e0000;
    --copper: #d0702a;
    --copper-dark: #a84f1a;
    --text-grey: #8a8a8a;
    --mark-grey: #5b5b5b;
    --back-grey: #6a6a6a;
    --white: #ffffff;
  }
  * { margin: 0; padding: 0; box-sizing: border-box; }
  html, body {
    width: 1200px; height: 1176px; overflow: hidden;
    background: var(--backdrop);
  }
  .canvas { position: relative; width: 1200px; height: 1176px; }
  .card {
    position: absolute; left: 281px; width: 617px; height: 353px;
    border-radius: 20px; overflow: hidden;
    box-shadow: 0 10px 18px rgba(0,0,0,0.45);
  }
  .card--front {
    top: 190px;
    background: linear-gradient(200deg, var(--card-white) 20%, var(--card-grey) 100%);
  }
  .card--back {
    top: 590px;
    background: radial-gradient(ellipse at 50% 40%, #1a0505 0%, var(--back-black) 70%);
  }
  .brand {
    position: absolute; left: 0; right: 0; text-align: center;
    font-family: 'Raleway', sans-serif; font-weight: 500;
  }
  .brand__square { display: block; margin: 0 auto; background: var(--copper); }
  .card--front .brand { top: 26px; }
  .card--front .brand__square { width: 48px; height: 48px; margin-bottom: 14px; }
  .card--front .brand__name { font-size: 26px; color: var(--mark-grey); }
  .card--back .brand { top: 84px; }
  .card--back .brand__square { width: 62px; height: 62px; margin-bottom: 22px; }
  .card--back .brand__name { font-size: 36px; color: var(--back-grey); }

  .info-band {
    position: absolute; left: 0; top: 168px; width: 100%; height: 127px;
    background: var(--band-black);
  }
  .person { position: absolute; left: 40px; top: 44px; font-family: 'Raleway', sans-serif; }
  .person__name { font-size: 18px; color: var(--text-grey); letter-spacing: 0.3px; }
  .person__name small { font-size: 14px; }
  .person__title { font-size: 13.5px; color: var(--copper); margin-top: 4px; letter-spacing: 0.2px; }
  .divider {
    position: absolute; left: 342px; top: 24px; width: 2px; height: 83px;
    background: var(--copper);
  }
  .contacts {
    position: absolute; left: 363px; top: 27px; list-style: none;
    font-family: 'Open Sans', sans-serif; font-size: 14.5px; color: var(--text-grey);
  }
  .contacts li { display: flex; align-items: center; height: 26.5px; }
  .contacts svg { width: 12px; height: 12px; margin-right: 8px; fill: var(--copper); }
  .address-band {
    position: absolute; left: 0; top: 298px; width: 100%; height: 22px;
    background: linear-gradient(180deg, var(--copper) 0%, var(--copper-dark) 100%);
    font-family: 'Open Sans', sans-serif; font-size: 13.5px; color: var(--white);
    text-align: center; line-height: 22px;
  }
</style>
</head>
<body>
<div class="canvas">
  <section class="card card--front">
    <div class="brand">
      <span class="brand__square"></span>
      <span class="brand__name">Pelton|Marsh &amp; Quillan</span>
    </div>
    <div class="info-band">
      <div class="person">
        <p class="person__name">DR. NEIL R. WHITCOMBE, <small>CFA</small></p>
        <p class="person__title">SCIENTIFIQUE DES FUSÉES FINANCIÈRES</p>
      </div>
      <span class="divider"></span>
      <ul class="contacts">
        <li><svg viewBox="0 0 12 12"><path d="M3 0.5 L5 3 L4 4.5 Q5 7 7.5 8 L9 7 L11.5 9 L10 11.5 Q4 11 0.5 2 Z"/></svg>000 000 0000</li>
        <li><svg viewBox="0 0 12 12"><path d="M0 2 H12 V10 H0 Z M1 3 L6 7 L11 3 Z" fill-rule="evenodd"/></svg>youremail@xyz.com</li>
        <li><svg viewBox="0 0 12 12"><path d="M6 0.5 A5.5 5.5 0 1 0 6 11.5 A5.5 5.5 0 1 0 6 0.5 Z M6 1.5 A4.5 4.5 0 1 1 6 10.5 A4.5 4.5 0 1 1 6 1.5 Z M1 5.5 H11 V6.5 H1 Z M5.5 1 H6.5 V11 H5.5 Z" fill-rule="evenodd"/></svg>www.yourwebsite.com</li>
      </ul>
    </div>
    <div class="address-band">0000, Somewhere, Anywhere, City, ST 0000</div>
  </section>

  <section class="card card--back">
    <div class="brand">
      <span class="brand__square"></span>
      <span class="brand__name">Pelton|Marsh &amp; Quillan</span>
    </div>
  </section>
</div>
</body>
</html>
```